Birthday Party Invitation for Jasper's 18th Birthday Party

Our eldest son Jasper is turning 18 and we are having a party at home to celebrate the occasion. This project is about creating an invitation that will go to our friends and family. We like things to be nicely designed so posting it to pixel harbor seemed to be the way to go.
The invitation needs to be able to be printed onto an A4 piece of paper. We have access to a color copier so it can be nice and bright.

We want an invitation that conveys a sense of occasion and looks as though we have put time and effort into having a great night to celebrate his 18th.
I have included some photo's of Jasper. They can go onto the invitation as is or they can be given some treatment to form a theme when on the invitiation. I'll leave the treatment of the photo's to the individual designer.

Target Market(s)

Friends and Family

Font styles to use
Sans Serif

Colors

Designer to choose colors to be used in the design.

Requirements
Must have
• The invitation must have the time, date and location of the party.
• Details:
• Saturday 29th of July 2017 7.00pm
• 41 Brackmere Lane, Fenwood
• Food and Drinks provided It must be bright and colourful and convey a sense of excitement.
Nice to have
• Inclusion of the photo's that I have uploaded.
Should not have
• any boring bits

```html
<!DOCTYPE html>
<html lang="en">
<head>
<meta charset="utf-8">
<title>Jasper's Eighteenth Birthday Invitation</title>
<link href="https://fonts.googleapis.com/css2?family=Allura&family=DM+Serif+Display&family=Josefin+Sans:wght@400&display=swap" rel="stylesheet">
<style>
  :root {
    --bg: #2b2b2b;
    --script: #d9d9d9;
    --glow: rgba(255, 255, 255, 0.55);
    --detail: #e4e4e4;
    --pink: #e8196e;
    --blue: #2aa3e0;
    --yellow: #ffe014;
    --green: #6cc43a;
    --orange: #f7941d;
    --teal: #14a39a;
  }
  html, body {
    margin: 0;
    padding: 0;
    overflow: hidden;
    background: var(--bg);
  }
  .invitation {
    position: relative;
    width: 846px;
    height: 1200px;
    background: var(--bg);
    overflow: hidden;
  }
  .numeral {
    position: absolute;
    left: 0;
    top: 0;
    width: 846px;
    height: 740px;
  }
  .numeral-text {
    font-family: "DM Serif Display", serif;
    font-size: 780px;
  }
  .headline {
    position: absolute;
    left: 0;
    top: 746px;
    width: 100%;
    margin: 0;
    text-align: center;
    white-space: nowrap;
    font-family: "Allura", cursive;
    font-weight: 400;
    font-size: 70px;
    line-height: 1.3;
    color: var(--script);
    text-shadow: 0 0 6px var(--glow), 0 0 14px var(--glow);
  }
  .details {
    position: absolute;
    left: 0;
    top: 876px;
    width: 100%;
    margin: 0;
    padding: 0;
    list-style: none;
    text-align: center;
    font-family: "Josefin Sans", sans-serif;
    font-size: 23px;
    letter-spacing: 1.6px;
    text-transform: uppercase;
    color: var(--detail);
    line-height: 33px;
  }
  .photo-strip {
    position: absolute;
    left: 29px;
    top: 1014px;
    display: flex;
    gap: 10px;
  }
  .photo {
    width: 123px;
    height: 135px;
  }
  .photo--sailing { background: linear-gradient(180deg, #a9c4dc, #3f7fa8); }
  .photo--harbour { background: linear-gradient(180deg, #8fb3d6, #3a4250); }
  .photo--blazer { background: linear-gradient(180deg, #8fb27a, #4a2a2e); }
  .photo--family { background: linear-gradient(180deg, #6f8a5a, #3d4d6a); }
  .photo--waterpolo { background: linear-gradient(180deg, #3fb3e0, #1f7fb8); }
  .photo--garden { background: linear-gradient(180deg, #5f7a45, #8a6a60); }
</style>
</head>
<body>
  <main class="invitation">
    <svg class="numeral" viewBox="0 0 846 740" role="img" aria-label="Large numeral 18 in bright party colours">
      <defs>
        <linearGradient id="partyColours" x1="0" y1="0" x2="1" y2="1">
          <stop offset="0" stop-color="var(--yellow)"/>
          <stop offset="0.2" stop-color="var(--pink)"/>
          <stop offset="0.4" stop-color="var(--blue)"/>
          <stop offset="0.6" stop-color="var(--green)"/>
          <stop offset="0.8" stop-color="var(--orange)"/>
          <stop offset="1" stop-color="var(--teal)"/>
        </linearGradient>
      </defs>
      <text class="numeral-text" x="428" y="698" text-anchor="middle" textLength="690" lengthAdjust="spacingAndGlyphs" fill="url(#partyColours)">18</text>
    </svg>

    <h1 class="headline">Jasper's Eighteenth Birthday</h1>

    <ul class="details">
      <li>Saturday 29th of July 2017 7.00pm</li>
      <li>41 Brackmere Lane, Fenwood</li>
      <li>Food and drinks provided</li>
    </ul>

    <div class="photo-strip">
      <div class="photo photo--sailing" role="img" aria-label="Photo of Jasper sailing a dinghy on the harbour"></div>
      <div class="photo photo--harbour" role="img" aria-label="Photo of Jasper in front of a harbour bridge"></div>
      <div class="photo photo--blazer" role="img" aria-label="Photo of Jasper in a striped school blazer"></div>
      <div class="photo photo--family" role="img" aria-label="Photo of Jasper in a tuxedo with his parents"></div>
      <div class="photo photo--waterpolo" role="img" aria-label="Photo of Jasper playing water polo in a pool"></div>
      <div class="photo photo--garden" role="img" aria-label="Photo of Jasper with a friend in a garden"></div>
    </div>
  </main>
</body>
</html>
```